Classy website for Corporate Entertainment - Action & Acrobatic Shows

12-Page Website to be coded using Wordpress!

We are "Velvet Summit Productions". We are all about providing 'experiences'! This website must be part of that experience :)

Please do not use our current website as inspiration for your design! We are looking for something new, and our business has outgrown that site (which was just for our shows) :)

We perform Action & Acrobatic Shows for corporate functions, as well as run Classes & Workshops from our Training Centre (Parkour, Acrobatics, etc), as well as Client Action Experiences and other services.

Example of our recent Morgan Vale 'Acrobatic Action Show' https://clipvault.example/watch/QxTr7nLpWzK

Our website must be super-classy/suave!! Needs to be heavily appealing to the Corporate community!

www.friendsphere.example/velvetsummitlive

Logo is available in the files below.
A series of photos have also been uploaded; please use any of these that you like throughout the design.

Menu Links from Home Page:
About Us (dropdown), Corporate Action Shows, Services (dropdown), Classes & Workshops (dropdown), The Ultimate Action Experience, Blog, Photos/Videos, Contact Us

PAGES:
- Home Page - must include a focus on Corporate Entertainment for the first glance, with information going down the page about our 4 major aspects: our Corporate Action Shows, Workshops & Classes, Services and Blog.

Required links on menu (menu does not necessarily have to be as a banner across the top - we are open to all ideas):

- Home Page

-"About Us" (dropdown with x2 pages "Our Shows" and "Our Team")

- Corporate Action Shows (x1 page)

- Services (dropdown with x3 pages "Action Showreels", and "Cosplay Competition Skits", and "Film & TV"

- Classes & Workshops (dropdown with x2 pages "Class Details & Prices" and "2016 Timetable"

- Ultimate Action Experience (x1 page with link to external website)

- Blog

- Videos & Photos or "See Us In Action" (x1 page)

- Contact Us

If you need more in-depth information into anything, please do not hesitate to send us a message!

Target Market(s)

Corporate (Classy)

Industry/Entity Type

Entertainment

Coding

Coded - Design and coding required

Number of Pages Required

5+ page

Requirements
Must have
• Website Coded via Wordpress

```html
<!DOCTYPE html>
<html lang="en">
<head>
<meta charset="utf-8">
<title>Velvet Summit Productions</title>
<link rel="stylesheet" href="https://fonts.googleapis.com/css2?family=Oswald:wght@400;500&family=Source+Sans+3:ital,wght@0,400;0,600;1,400&display=swap">
<style>
:root{
  --ink:#1f1f1f;
  --panel:#232323;
  --paper:#f1f1f1;
  --white:#ffffff;
  --red:#d8262b;
  --muted:#cfcfcf;
  --grey-text:#555;
}
*{box-sizing:border-box;margin:0;padding:0}
html,body{width:1200px;height:2281px;overflow:hidden}
body{position:relative;background:var(--white);font-family:"Source Sans 3",Arial,sans-serif;color:var(--ink)}
.abs{position:absolute}
.display{font-family:"Oswald","Arial Narrow",sans-serif;text-transform:uppercase;letter-spacing:1px}

.topbar{left:0;top:0;width:1200px;height:24px;background:var(--ink);color:var(--white);font-size:10px;text-align:center;line-height:24px;letter-spacing:1.5px}
.masthead{left:0;top:24px;width:1200px;height:165px;background:var(--paper);display:flex;align-items:center;justify-content:center;gap:14px}
.brand-mark{width:26px;height:26px;background:var(--ink)}
.brand-name{font-family:"Oswald","Arial Narrow",sans-serif;font-weight:500;font-size:34px;letter-spacing:2px;text-transform:uppercase;color:var(--ink)}

.mainnav{left:0;top:189px;width:1200px;height:62px;background:var(--panel)}
.mainnav a{position:absolute;top:0;line-height:62px;font-size:12.5px;font-weight:400;color:var(--white);text-decoration:none}
.mainnav a.active{color:var(--red)}

.hero{left:0;top:251px;width:1200px;height:374px;
  background:
    radial-gradient(ellipse 260px 220px at 720px 150px,rgba(210,170,140,.45),rgba(210,170,140,0) 100%),
    linear-gradient(180deg,#1d1a19 0%,#2a2320 40%,#5a3422 62%,#8a4a2a 80%,#6a3520 100%)}
.slide-arrow{width:47px;height:62px;background:var(--ink);display:flex;align-items:center;justify-content:center}
.hero-caption{left:163px;top:563px;width:1037px;height:62px;background:rgba(31,31,31,.94)}
.hero-caption h1{position:absolute;left:22px;top:0;line-height:62px;font-size:18px;font-weight:400;color:var(--white);letter-spacing:1.5px}
.btn{position:absolute;border:1.5px solid var(--white);color:var(--white);font-family:"Oswald","Arial Narrow",sans-serif;font-size:12.5px;text-transform:uppercase;letter-spacing:1px;display:flex;align-items:center;justify-content:center;text-decoration:none}
.btn.red{border-color:var(--red);color:var(--red)}

.feature{left:163px;top:651px;width:874px;height:490px;background:var(--panel)}
.feature-copy{position:absolute;left:0;top:0;width:290px;height:490px;padding:22px 24px;color:var(--muted);font-size:9.6px;line-height:1.3}
.feature-copy h2{font-size:12.5px;color:var(--white);font-weight:500;margin-bottom:18px}
.feature-copy p{margin-bottom:13px}
.feature-photo{position:absolute;left:290px;top:0;width:584px;height:490px;
  background:
    radial-gradient(ellipse 200px 260px at 400px 220px,rgba(235,235,235,.55),rgba(235,235,235,0) 100%),
    radial-gradient(ellipse 300px 120px at 150px 330px,rgba(150,150,150,.35),rgba(150,150,150,0) 100%),
    linear-gradient(180deg,#151515 0%,#2c2c2c 45%,#4a4a4a 75%,#2a2a2a 100%)}

.tiles{left:0;top:1167px;width:1200px;height:633px;background:var(--paper)}
.tile{position:absolute;width:424px;height:279px;background:var(--panel)}
.tile-photo{position:absolute;left:0;top:0;width:424px}
.tile h3{position:absolute;left:24px;font-size:12.5px;font-weight:400;color:var(--white)}
.tile p{position:absolute;left:24px;top:196px;width:376px;font-size:9.6px;line-height:1.3;color:var(--muted)}

.testimonials{left:0;top:1800px;width:1200px;height:250px;background:var(--white);text-align:center}
.testimonials h2{position:absolute;left:0;top:24px;width:1200px;font-size:16px;font-weight:400;letter-spacing:1.5px;color:var(--ink)}
.quote-name{position:absolute;left:0;top:100px;width:1200px;font-size:10px;color:var(--grey-text)}
.quote{position:absolute;left:388px;top:113px;width:424px;font-size:11px;font-style:italic;line-height:1.3;color:var(--grey-text)}
.dots{position:absolute;left:565px;top:224px;display:flex;gap:5px}
.dots span{width:13px;height:2px;background:#bbb}

.footer{left:0;top:2050px;width:1200px;height:231px;background:var(--panel);color:var(--muted)}
.footer .brand{position:absolute;left:163px;top:52px;font-family:"Oswald","Arial Narrow",sans-serif;font-weight:500;font-size:14px;color:var(--white);letter-spacing:1px;text-transform:uppercase;line-height:1.1;width:130px}
.footer .legal{position:absolute;left:163px;top:100px;font-size:8.5px;line-height:1.25}
.fcol{position:absolute;top:50px}
.fcol h4{font-family:"Oswald","Arial Narrow",sans-serif;font-weight:400;font-size:12px;letter-spacing:1px;text-transform:uppercase;color:var(--white);margin-bottom:6px}
.fcol li{list-style:none;font-size:9.5px;line-height:15px}
.fcol address{font-style:normal;font-size:9.5px;line-height:12px}
.social{display:flex;gap:6px;margin-top:8px}
.social span{width:16px;height:16px;border-radius:50%;background:var(--white)}
</style>
</head>
<body>

<div class="abs topbar display">• Ultimate Action Experience •</div>

<header class="abs masthead">
  <span class="brand-mark"></span>
  <span class="brand-name">Velvet Summit Productions</span>
</header>

<nav class="abs mainnav display">
  <a class="active" style="left:163px">About ›</a>
  <a style="left:266px">Corporate Action Shows</a>
  <a style="left:473px">Services ›</a>
  <a style="left:596px">Classes &amp; Workshops ›</a>
  <a style="left:794px">Blog</a>
  <a style="left:884px">Gallery</a>
  <a style="left:990px">Contact</a>
</nav>

<section class="abs hero" role="img" aria-label="Two performers in formal wear mid acrobatic throw on a wood-panelled stage"></section>
<div class="abs slide-arrow" style="left:0;top:406px"><svg width="16" height="30"><polyline points="14,2 2,15 14,28" fill="none" stroke="#fff" stroke-width="1.5"/></svg></div>
<div class="abs slide-arrow" style="left:1153px;top:406px"><svg width="16" height="30"><polyline points="2,2 14,15 2,28" fill="none" stroke="#fff" stroke-width="1.5"/></svg></div>
<div class="abs hero-caption">
  <h1 class="display">2016 - Morgan Vale Acrobatic Action Show</h1>
  <a class="btn" style="left:770px;top:12px;width:92px;height:38px">Read More</a>
</div>

<section class="abs feature">
  <div class="feature-copy">
    <h2 class="display">Corporate Action Shows</h2>
    <p>Velvet Summit specialises in corporate class entertainment, performing our unique 'Acrobatic Action' Shows.</p>
    <p>Lorem ipsum dolor sit amet, consectetur adipisicing elit, sed do eiusmod tempor incididunt ut labore et dolore magna aliqua. Ut enim ad minim veniam, quis nostrud exercitation ullamco laboris nisi ut aliquip ex ea commodo consequat. Duis aute irure dolor in reprehenderit in voluptate velit esse cillum dolore eu fugiat nulla pariatur. Excepteur sint occaecat cupidatat non proident, sunt in culpa qui officia deserunt mollit anim id est laborum.</p>
    <p>Sed ut perspiciatis unde omnis iste natus error sit voluptatem accusantium doloremque laudantium, totam rem aperiam, eaque ipsa quae ab illo inventore veritatis et quasi architecto beatae vitae dicta sunt explicabo. Nemo enim ipsam voluptatem quia voluptas sit aspernatur aut odit aut fugit, sed quia consequuntur magni dolores eos qui ratione voluptatem sequi nesciunt. Neque porro quisquam est, qui dolorem ipsum quia dolor sit amet, consectetur, adipisci velit, sed quia non numquam eius modi tempora incidunt ut labore et dolore magnam aliquam quaerat voluptatem.</p>
    <a class="btn" style="left:24px;top:429px;width:94px;height:37px">Read More</a>
  </div>
  <div class="feature-photo" role="img" aria-label="Black and white photo of a performer in a bow tie striking an action pose on stage"></div>
</section>

<section class="abs tiles">
  <article class="tile" style="left:163px;top:25px">
    <div class="tile-photo" role="img" aria-label="Silhouettes of two martial artists sparring with staffs at sunset" style="height:124px;background:linear-gradient(180deg,#4e5a6c 0%,#8a8078 45%,#d49248 78%,#f0b040 100%)"></div>
    <h3 class="display" style="top:146px">Workshops &amp; Classes</h3>
    <a class="btn red" style="left:319px;top:134px;width:92px;height:37px">Read More</a>
    <p>Want to learn our craft? Check out our timetables and pricing for our workshops &amp; classes... Lorem ipsum dolor sit amet, consectetur adipisicing elit, sed do eiusmod tempor incididunt ut labore et dolore magna aliqua. Ut enim ad minim veniam, quis nostrud exercitation ullamco laboris nisi ut aliquip ex ea commodo consequat.</p>
  </article>
  <article class="tile" style="left:613px;top:25px">
    <div class="tile-photo" role="img" aria-label="Crowded banquet hall under pink and purple event lighting" style="height:218px;background:radial-gradient(ellipse 180px 80px at 280px 110px,rgba(140,150,220,.45),rgba(140,150,220,0)),linear-gradient(180deg,#8a3a50 0%,#5a2a48 50%,#1e1a26 100%)"></div>
    <h3 class="display" style="top:236px">Services We Offer</h3>
    <a class="btn" style="left:319px;top:224px;width:92px;height:37px">Read More</a>
  </article>
  <article class="tile" style="left:163px;top:330px">
    <div class="tile-photo" role="img" aria-label="Silhouettes of three performers in hats posing with hand pistols" style="height:217px;background:radial-gradient(ellipse at 50% 40%,#7a7a7a,#1e1e1e 75%)"></div>
    <h3 class="display" style="top:235px">Our Blog</h3>
    <a class="btn" style="left:319px;top:223px;width:92px;height:37px">Read More</a>
  </article>
  <article class="tile" style="left:613px;top:330px">
    <div class="tile-photo" role="img" aria-label="Black and white photo of guests dancing in a ballroom under spotlights" style="height:217px;background:radial-gradient(ellipse 120px 60px at 340px 40px,rgba(230,230,230,.5),rgba(230,230,230,0)),linear-gradient(180deg,#2e2e2e 0%,#555 60%,#2a2a2a 100%)"></div>
    <h3 class="display" style="top:235px">Get In Touch With Us</h3>
    <a class="btn" style="left:319px;top:223px;width:92px;height:37px">Read More</a>
  </article>
</section>

<section class="abs testimonials">
  <h2 class="display">Testimonials</h2>
  <div class="abs slide-arrow" style="left:0;top:95px"><svg width="16" height="30"><polyline points="14,2 2,15 14,28" fill="none" stroke="#fff" stroke-width="1.5"/></svg></div>
  <div class="abs slide-arrow" style="left:1153px;top:95px"><svg width="16" height="30"><polyline points="2,2 14,15 2,28" fill="none" stroke="#fff" stroke-width="1.5"/></svg></div>
  <div class="quote-name">— Priya Halden —</div>
  <p class="quote">"This was great fun! The guys and girls at VelvetSummit were super friendly and professional. The show was awesome and in my opinion, was the highlight of the evening. Definitely would recommend!"</p>
  <div class="dots"><span></span><span></span><span></span><span></span></div>
</section>

<footer class="abs footer">
  <div class="brand">Velvet Summit Productions</div>
  <p class="legal">© Velvet Summit Productions 2016.<br>All Rights Reserved</p>
  <div class="fcol" style="left:475px">
    <h4>Services</h4>
    <ul>
      <li>Corporate Action Shows</li><li>Class Details &amp; Prices</li><li>Workshop Timetable</li><li>Action Showreels</li><li>Cosplay Competition Skits</li><li>Film &amp; TV</li><li>Ultimate Action Experience</li>
    </ul>
  </div>
  <div class="fcol" style="left:748px">
    <h4>Company</h4>
    <ul><li>Home</li><li>Our Shows</li><li>Our Team</li><li>Blog</li><li>Gallery</li></ul>
  </div>
  <div class="fcol" style="left:972px">
    <h4>Contact</h4>
    <ul><li style="text-decoration:underline;color:var(--white)">Contact Us</li></ul>
    <address>18 Lantern Rd,<br>Riverton<br>NSW 2600</address>
    <h4 style="margin-top:14px">Follow Us</h4>
    <div class="social"><span></span><span></span><span></span></div>
  </div>
</footer>

</body>
</html>
```